FACE HARBOR

Labels for Men's Skin Care. Organic, target 25-35 The label will be 2x3.5 on a 4oz amber bottle. 3 labels with the information shown on the uploaded sample.
Our product is a e-commerce built to help my 24 year old twin sons have a business of their own. Although it will be sold online they will also do foot work and sell to barbers at barber shops using as a mist on customers after shaving. So we want something that will attract male customers and will look good in a modern Barbershop. This is there shot and packaging is very very important. So if you could help us out with a great label we would be working with you in the future for package design. Our line will have several mens Organic natural skin care cleanser, mask toners and moisturizers..Thank you for your help. We also hope to put our products in beauty supply shops. So it needs to stand out as a mans product but still be traditional male product. Oh be creative mind that you are and remember we are trying to build a brand that attracts 25-35 male. Thank you

Hello, I just wanted to let you know that I am up working very late.

for anyone on the other side of the world up and working. I sleep about
3 hours.. So I'll be up for a few more hours and then up again around 5am my time

Good morning... I just wanted to say I will need three labels.. The words on all three are not that different and will fit pretty much the same on all three. So if you could work with one showing how the colors might be a little different on the other two you can do that with just the one label Just to make it easier on you if you like.. we can fix the other two once I find the right label,  Thank you it is 3am here.. still working.. I love it.

Target Market(s)

MALE 25-35

Industry/Entity Type

E-Commerce

Requirements
Must have
• final design must be fitted to the dieline uploaded.

```html
<!DOCTYPE html>
<html lang="en">
<head>
<meta charset="utf-8">
<title>Face Harbor – Men's Skin Care Labels</title>
<link rel="stylesheet" href="https://fonts.googleapis.com/css2?family=Cinzel:wght@500&family=Old+Standard+TT&family=Bebas+Neue&display=swap">
<style>
  :root {
    --page: #ffffff;
    --label-edge: #2c1b20;
    --label-ground: #321e25;
    --band: #2a181d;
    --gold: #d9ab68;
    --gold-light: #f2cf8e;
    --gold-deep: #a8733a;
    --rust: #6e3a27;
    --rust-deep: #4d2519;
    --chip: #5c2e22;
  }
  * { margin: 0; padding: 0; box-sizing: border-box; }
  html, body { width: 1200px; height: 1000px; overflow: hidden; background: var(--page); }
  .canvas { position: relative; width: 1200px; height: 1000px; }

  .label {
    position: absolute; top: 226px; width: 344px; height: 601px;
    background: var(--label-edge);
  }
  .label--shave { left: 37px; }
  .label--berry { left: 429px; }
  .label--fresh { left: 821px; }

  .label__frame {
    position: absolute; inset: 8px;
    border: 5px solid var(--gold);
    border-image: linear-gradient(135deg, var(--gold-deep), var(--gold-light) 45%, var(--gold-deep)) 1;
    background: var(--label-ground);
    overflow: hidden;
  }
  .label__mark {
    position: absolute; top: 52px; left: 50%; width: 58px; height: 58px;
    margin-left: -29px; border-radius: 50%; background: var(--gold);
  }
  .label__brand {
    position: absolute; top: 116px; left: 0; right: 0; text-align: center;
    font-family: "Cinzel", serif; font-weight: 500; font-size: 38px;
    color: var(--gold); letter-spacing: 0.5px;
  }
  .label__pattern {
    position: absolute; left: 0; right: 0; top: 330px; bottom: 0;
    background: linear-gradient(180deg, rgba(110,58,39,0) 0%, rgba(110,58,39,0.35) 30%, var(--rust) 62%, var(--rust-deep) 100%);
  }
  .label__claim {
    position: absolute; top: 216px; left: 0; right: 0; text-align: center;
    font-family: "Old Standard TT", serif; font-size: 23px; line-height: 34px;
    color: var(--gold);
  }
  .label__band {
    position: absolute; top: 381px; left: 0; right: 0; height: 60px;
    background: var(--band); text-align: center;
    font-family: "Bebas Neue", sans-serif; font-size: 35px; line-height: 60px;
    color: var(--gold); letter-spacing: 0.3px;
  }
  .label__details {
    position: absolute; top: 491px; left: 0; right: 0; text-align: center;
  }
  .label__ingredients, .label__volume {
    display: inline-block; background: var(--chip);
    font-family: "Old Standard TT", serif; color: var(--gold);
  }
  .label__ingredients { font-size: 17px; line-height: 26px; padding: 0 5px; }
  .label__volume { font-size: 23px; line-height: 30px; padding: 0 10px; margin-top: 6px; }
</style>
</head>
<body>
<main class="canvas">

  <section class="label label--shave">
    <div class="label__frame">
      <div class="label__pattern" role="img" aria-label="Soft brown leaf and swirl pattern across the lower label"></div>
      <span class="label__mark"></span>
      <h2 class="label__brand">FACE HARBOR</h2>
      <p class="label__claim">Treat &amp; Prevent<br>Ingrown Hair +<br>Calms Razor Burn<br>After Shaving</p>
      <p class="label__band">BOTANICAL HEALING MILK</p>
      <div class="label__details">
        <span class="label__ingredients">Acai Berry + Goats Milk</span><br>
        <span class="label__volume">3.5 fl oz 103 ml</span>
      </div>
    </div>
  </section>

  <section class="label label--berry">
    <div class="label__frame">
      <div class="label__pattern" role="img" aria-label="Soft brown leaf and swirl pattern across the lower label"></div>
      <span class="label__mark"></span>
      <h2 class="label__brand">FACE HARBOR</h2>
      <p class="label__claim">Maintain Groin<br>Freshness &amp; Dryness<br>While Reducing Skin<br>Irritation &amp; Chafing</p>
      <p class="label__band">BOTANICAL HEALING MILK</p>
      <div class="label__details">
        <span class="label__ingredients">Cranberry + Pomogrenate</span><br>
        <span class="label__volume">3.5 fl oz 103 ml</span>
      </div>
    </div>
  </section>

  <section class="label label--fresh">
    <div class="label__frame">
      <div class="label__pattern" role="img" aria-label="Soft brown leaf and swirl pattern across the lower label"></div>
      <span class="label__mark"></span>
      <h2 class="label__brand">FACE HARBOR</h2>
      <p class="label__claim">Maintain Groin<br>Freshness &amp; Dryness<br>While Reducing Skin<br>Irritation &amp; Chafing</p>
      <p class="label__band">MANHOOD FRESHNER</p>
      <div class="label__details">
        <span class="label__ingredients">Organic Natural Healing</span><br>
        <span class="label__volume">3.5 fl oz 103 ml</span>
      </div>
    </div>
  </section>

</main>
</body>
</html>
```